Velmont Recycling needs a new web design

We need a new web design for our company based in Austin, TX. We resell and recycling electronics such as laptops, computer components, Zelvos, Quorbs, etc. Since our inception over ten years ago, we’ve become one of the premier electronics recycling and remarketing companies in Austin, Texas.

```html
<!DOCTYPE html>
<html lang="en">
<head>
<meta charset="utf-8">
<title>Velmont Recycling</title>
<link rel="stylesheet" href="https://fonts.googleapis.com/css2?family=Open+Sans:wght@400;600;700&family=Playfair+Display:wght@700;900&display=swap">
<style>
:root{
  --blue:#1f62b3;
  --navy:#15345e;
  --orange:#f47a36;
  --ink:#555b63;
  --muted:#8a9098;
  --rule:#e3e6ea;
  --panel:#f1f1f1;
  --soft:#f3f5f8;
  --footer:#343434;
  --footer-line:#4a4a4a;
  --footer-text:#c9c9c9;
  --base:#e9e9e9;
  --ghost:#f2f3f5;
  --badge:#eceef1;
}
*{box-sizing:border-box;margin:0;padding:0}
html,body{width:1200px;height:2699px;overflow:hidden}
body{position:relative;background:#fff;font-family:"Open Sans",Arial,sans-serif;color:var(--ink)}
.abs{position:absolute}

/* header */
.site-header{left:0;top:0;width:1200px;height:50px;background:#fff;border-top:3px solid var(--blue)}
.brand{left:162px;top:8px;display:flex;align-items:center;gap:8px}
.brand-dot{width:30px;height:30px;border-radius:50%;background:var(--navy)}
.brand-name{font-size:15px;font-weight:700;color:var(--navy);line-height:1.1;width:100px}
.main-nav{left:526px;top:0;height:47px;display:flex;align-items:center}
.main-nav a{font-size:10px;color:#4d5560;text-decoration:none;padding:0 11px;line-height:47px;position:relative;white-space:nowrap}
.main-nav a.active{color:var(--blue)}
.main-nav a.active::before{content:"";position:absolute;left:50%;top:-3px;margin-left:-8px;border:8px solid transparent;border-top-color:var(--blue);border-bottom:0}
.head-btn{top:10px;width:38px;height:32px;background:var(--orange);display:flex;align-items:center;justify-content:center}

/* hero */
.hero-photo{left:0;top:50px;width:1200px;height:504px;background:linear-gradient(180deg,rgba(0,0,0,0) 72%,#6d6966 74%,#575351 100%),radial-gradient(ellipse at 62% 40%,#eef0f2 0%,#c9cccf 45%,#8d9093 85%)}
.hero-title{left:162px;top:180px;font-family:"Playfair Display",Georgia,serif;font-weight:900;font-size:50px;color:#111;letter-spacing:1px;line-height:1.1}
.hero-tag{left:164px;top:240px;font-size:11.5px;letter-spacing:7.4px;color:var(--blue);font-weight:600}
.hero-copy{left:162px;top:276px;width:345px;font-size:12px;line-height:18.5px;color:#fff}
.search-input{left:160px;top:502px;width:740px;height:41px;background:#fff;font-size:10px;color:#777;padding:13px 12px}
.search-btn{left:910px;top:502px;width:128px;height:41px;background:var(--orange);color:#fff;font-size:12px;font-weight:700;text-align:center;line-height:41px}

/* section heads */
.ghost{left:0;width:1200px;text-align:center;font-family:"Playfair Display",Georgia,serif;font-weight:700;font-size:48px;color:var(--ghost)}
.sec-title{left:0;width:1200px;text-align:center;font-size:19px;font-weight:600;color:var(--blue)}
.rule{left:162px;width:876px;height:2px;background:var(--rule)}

/* about */
.about-card{left:246px;top:693px;width:706px;height:151px;border:1px solid #dde1e5;border-radius:6px;box-shadow:0 2px 6px rgba(0,0,0,.06);padding:30px 22px 0;text-align:center;font-size:11px;line-height:18px;color:var(--muted)}
.about-links{left:515px;top:824px;display:flex;gap:12px;font-size:10px;font-weight:700}
.about-links span{padding-bottom:4px}
.about-links .more{color:var(--navy);border-bottom:2px solid var(--blue)}
.about-links .book{color:var(--orange);border-bottom:2px solid var(--orange)}

/* services */
.svc-photo{top:1047px;width:297px;height:246px}
.svc-shadow{top:1300px;width:297px;height:22px;background:radial-gradient(ellipse at center,rgba(0,0,0,.12),rgba(0,0,0,0) 70%)}

/* capability */
.cap{left:162px;top:1459px;width:876px;height:223px;background:var(--panel)}
.cap-col{top:1459px;height:223px;padding:13px 10px 0 10px}
.cap-col h4{font-size:9.5px;font-weight:700;color:#222;text-transform:uppercase;padding-bottom:4px;position:relative;margin-bottom:6px}
.cap-col h4::after{content:"";position:absolute;left:0;bottom:0;width:36px;height:2px;background:var(--orange)}
.cap-col ul{list-style:none}
.cap-col li{font-size:9.5px;line-height:12px;color:#555;padding:3px 0 3px 10px;border-bottom:1px dashed #b8b8b8;position:relative}
.cap-col li::before{content:"";position:absolute;left:2px;top:8px;width:3px;height:3px;border-radius:50%;background:#555}
.cap-feature{left:505px;top:1459px;width:189px;height:223px;background:var(--orange);color:#fff;text-align:center}
.cap-feature small{display:block;margin-top:60px;font-size:12px;letter-spacing:.5px}
.cap-feature strong{display:block;font-family:"Playfair Display",Georgia,serif;font-weight:700;font-size:44px;line-height:52px}

/* certified */
.badge{top:1873px;height:104px;border:1px dashed #d4d8dc;display:flex;align-items:center;justify-content:center}
.badge-mark{width:240px;height:62px;border-radius:4px;background:var(--badge)}

/* contact */
.contact{left:0;top:2030px;width:1200px;height:381px;background:var(--soft)}
.field{background:#fff;border-radius:5px}
.submit{left:263px;top:2306px;width:674px;height:38px;background:var(--orange);border-radius:5px;color:#fff;font-size:10px;font-weight:700;text-align:center;line-height:38px}

/* footer */
.footer{left:0;top:2411px;width:1200px;height:252px;background:var(--footer)}
.social{top:2423px;width:29px;height:29px}
.foot-line{left:0;top:2465px;width:1200px;height:1px;background:var(--footer-line)}
.foot-top{top:2431px;font-size:10.5px;color:var(--footer-text);display:flex;align-items:center;gap:8px}
.foot-col{top:2485px;font-size:10.5px;color:var(--footer-text)}
.foot-col h5{font-size:11px;font-weight:700;color:#fff;margin-bottom:14px;letter-spacing:.3px}
.foot-col p{line-height:18px}
.foot-row{display:flex;gap:10px;margin-bottom:12px}
.news{left:786px;top:2515px;width:254px;height:36px;background:#fff;font-size:10px;font-style:italic;color:#999;padding:11px 12px}
.copy{left:0;top:2663px;width:1200px;height:36px;background:var(--base);text-align:center;font-size:9.5px;line-height:36px;color:#555}
</style>
</head>
<body>

<header class="abs site-header">
  <div class="abs brand"><span class="brand-dot"></span><span class="brand-name">Velmont Recycling</span></div>
  <nav class="abs main-nav">
    <a class="active">HOME</a><a>ABOUT US</a><a>OUR SERVICES</a><a>BOOK ONLINE</a><a>CONTACT US</a>
  </nav>
  <div class="abs head-btn" style="left:959px">
    <svg width="14" height="14" viewBox="0 0 14 14"><circle cx="7" cy="4.5" r="3" fill="#fff"/><path d="M1 14c0-4 3-6 6-6s6 2 6 6z" fill="#fff"/></svg>
  </div>
  <div class="abs head-btn" style="left:1000px">
    <svg width="14" height="14" viewBox="0 0 14 14"><circle cx="6" cy="6" r="4.2" fill="none" stroke="#fff" stroke-width="2"/><path d="M9 9l4 4" stroke="#fff" stroke-width="2.2"/></svg>
  </div>
</header>

<section>
  <div class="abs hero-photo" role="img" aria-label="Photo of a blue recycling bin filled with old keyboards, cables and circuit boards against a grey wall"></div>
  <h1 class="abs hero-title">COMPUTER</h1>
  <div class="abs hero-tag">RECYCLING MADE EASY</div>
  <p class="abs hero-copy">Want to make a difference to our environment and planet? Velmont Recycling is here to help! Velmont recycling has been helping keep the environment healthy since 2006, we specialize in recycling services that help citizens become experts at reducing waste. We have a passion to keep our world clean and are here to guide you through all the stages of the recycling process.</p>
  <div class="abs search-input">What Are You Looking For</div>
  <div class="abs search-btn">SEARCH</div>
</section>

<section>
  <div class="abs ghost" style="top:608px">About Velmont Recycling</div>
  <h2 class="abs sec-title" style="top:626px">About Velmont Recycling</h2>
  <div class="abs about-card">What most people do not realize is electronic waste represents 2% of America's trash in landfills, but it equals 70% of overall toxic waste. Used computer equipment is a rapidly growing source of waste across the country. Only 12.5% of electronic waste is currently recycled in the US. Computers contain valuable parts that we can recycle, and heavy metals that we should try to keep out of landfills. Despite this, Texas has historically had low computer recycling rates in the past.</div>
  <div class="abs about-links"><span class="more">LEARN MORE</span><span class="book">BOOK ONLINE</span></div>
  <div class="abs rule" style="top:911px"></div>
</section>

<section>
  <div class="abs ghost" style="top:955px">Our Services</div>
  <h2 class="abs sec-title" style="top:973px">Our Services</h2>
  <div class="abs svc-photo" style="left:273px;background:linear-gradient(160deg,#e4e1da,#bdb7ac 60%,#8e8a84)" role="img" aria-label="Photo of stacked old computer monitors, towers and keyboards"></div>
  <div class="abs svc-photo" style="left:630px;background:linear-gradient(160deg,#d9d3c6,#a9a197 55%,#4b4f57)" role="img" aria-label="Photo of an adult and a child dropping electronics into a recycling bin"></div>
  <div class="abs svc-shadow" style="left:273px"></div>
  <div class="abs svc-shadow" style="left:630px"></div>
  <div class="abs rule" style="top:1390px"></div>
</section>

<section>
  <div class="abs cap"></div>
  <div class="abs cap-col" style="left:162px;width:164px">
    <h4>Recycling</h4>
    <ul><li>Certified Global Recycling Capabilities</li><li>Sort by commodity</li><li>Certificate of Recycling</li><li>Data Destruction</li><li>Verifiable Certified Down stream Vendors</li></ul>
  </div>
  <div class="abs" style="left:327px;top:1459px;width:5px;height:223px;background:#fff"></div>
  <div class="abs cap-col" style="left:333px;width:172px">
    <h4>Logistics</h4>
    <ul><li>Global Logistics Support</li><li>Global Warehouse Capabilities</li><li>Global Audit Capabilities</li><li>Inventory Management</li><li>Asset Management</li><li>Bill of Lading</li><li>Proof of Delivery</li><li>Transfer of Ownership (TOO)</li></ul>
  </div>
  <div class="abs cap-feature"><small>CAPABILITY</small><strong>OVER<br>VIEW</strong></div>
  <div class="abs cap-col" style="left:698px;width:168px">
    <h4>Certificates</h4>
    <ul><li>R2:2013 Responsible Recycling Certified</li><li>ISO 14001:2015</li><li>OHSAS 18001:2007</li><li>Lone Prairie Environmental Board (LPEB)</li><li>Regulated Entity # RN104582271</li><li>GDPR Compliant</li><li>HIPPA Compliant</li></ul>
  </div>
  <div class="abs" style="left:866px;top:1459px;width:5px;height:223px;background:#fff"></div>
  <div class="abs cap-col" style="left:871px;width:167px">
    <h4>Return:</h4>
    <ul><li>Market Value Pricing</li><li>Profit Sharing</li></ul>
  </div>
  <div class="abs rule" style="top:1749px"></div>
</section>

<section>
  <div class="abs ghost" style="top:1792px">We Are Certified</div>
  <h2 class="abs sec-title" style="top:1810px">We Are Certified</h2>
  <div class="abs badge" style="left:234px;width:351px">
    <div class="badge-mark" role="img" aria-label="Norvane Registrar, Inc. certification badge"></div>
  </div>
  <div class="abs badge" style="left:613px;width:290px">
    <div class="badge-mark" style="width:220px" role="img" aria-label="Lone Prairie Environmental Board certification badge"></div>
  </div>
</section>

<section>
  <div class="abs contact"></div>
  <div class="abs ghost" style="top:2074px;color:#fff">Contact Us</div>
  <h2 class="abs sec-title" style="top:2092px">Contact Us</h2>
  <div class="abs field" style="left:263px;top:2159px;width:327px;height:38px"></div>
  <div class="abs field" style="left:610px;top:2159px;width:327px;height:38px"></div>
  <div class="abs field" style="left:263px;top:2215px;width:674px;height:73px"></div>
  <div class="abs submit">SUBMIT</div>
</section>

<footer>
  <div class="abs footer"></div>
  <div class="abs social" style="left:162px;background:#3b5a9a"></div>
  <div class="abs social" style="left:196px;background:#2aa3e0"></div>
  <div class="abs social" style="left:230px;background:#d9452f"></div>
  <div class="abs social" style="left:264px;background:#1a7db8"></div>
  <div class="abs social" style="left:298px;background:#f07a2c"></div>
  <div class="abs foot-top" style="left:772px">
    <svg width="8" height="12" viewBox="0 0 8 12"><path d="M2 0h2l1 3-2 1c0 2 1 3 2 4l2-1 1 2v2c-4 0-8-5-8-9z" fill="#c9c9c9"/></svg>(512)555-0147</div>
  <div class="abs foot-top" style="left:898px">
    <svg width="13" height="9" viewBox="0 0 13 9"><rect x=".5" y=".5" width="12" height="8" fill="none" stroke="#c9c9c9"/><path d="M.5 .5l6 4.5 6-4.5" fill="none" stroke="#c9c9c9"/></svg>dana@velmontrecycling.com</div>
  <div class="abs foot-line"></div>

  <div class="abs foot-col" style="left:162px;width:250px">
    <h5>CONTACT US</h5>
    <div class="foot-row"><svg width="9" height="13" viewBox="0 0 9 13"><path d="M4.5 0a4.5 4.5 0 0 1 4.5 4.5C9 8 4.5 13 4.5 13S0 8 0 4.5A4.5 4.5 0 0 1 4.5 0z" fill="#9a9a9a"/><circle cx="4.5" cy="4.5" r="1.6" fill="#343434"/></svg><p>4120 Brindle Oak Ave<br>Austin TX USA 78759</p></div>
    <div class="foot-row"><svg width="12" height="10" viewBox="0 0 12 10"><rect x="0" y="3" width="12" height="7" rx="1" fill="#9a9a9a"/><rect x="2" y="0" width="8" height="3" fill="#9a9a9a"/></svg><p>Phone: (512)555-0147</p></div>
    <div class="foot-row"><svg width="12" height="9" viewBox="0 0 12 9"><rect x=".5" y=".5" width="11" height="8" fill="none" stroke="#9a9a9a"/><path d="M.5 .5l5.5 4 5.5-4" fill="none" stroke="#9a9a9a"/></svg><p>E-mail: dana@velmontrecycling.com</p></div>
  </div>
  <div class="abs foot-col" style="left:457px">
    <h5>SITE MAP</h5>
    <p>Privacy Policy<br>Terms &amp; Condition</p>
  </div>
  <div class="abs foot-col" style="left:604px">
    <h5>USEFUL LINKS</h5>
    <p>Home<br>About Us<br>Our Services<br>Book Online<br>Contact Us</p>
  </div>
  <div class="abs foot-col" style="left:786px">
    <h5>NEWSLETTER SIGN UP</h5>
  </div>
  <div class="abs news">Email</div>
  <svg class="abs" style="left:1012px;top:2527px" width="16" height="12" viewBox="0 0 16 12"><path d="M0 6l16-6-3 12-5-4z" fill="#c4c4c4"/></svg>
  <div class="abs copy">©2016 Velmontrecycling, Allrights are Reserved</div>
</footer>

</body>
</html>
```